Brontaro Web Site

Redesigned web site for Brontaro Ltd (www.brontaro-example.co.uk). This is to feature new logo (attached). Brontaro Ltd is a company which specialises in Geographic Information Systems and Geographic data - we call ourselves GIS Data Specialists. We are looking for something which conveys our professionalism and our experience. There will be more pages than on the current Brontaro website. There will be: Home, Data Migration, Data Cleansing & Validation, Data Analysis, Data Maintenance, Data Quality and an About Us page. All these should be accessible from each page on the website.
Updates
I didn't really think to say that the content of the web site is going to change from the current one we have. There will be more pages than on the current one. They will be: Home, Data Migration, Data Cleansing & Validation, Data Analysis, Data Maintenance, Data Quality and an About Us page. All these should be accessible from each page on the website. I didn't really think through the fact that the number of pages / areas to access can influence the layout of the site, sorry.
Target Market(s)
Utility Companies (e.g. telecommunications providers, energy companies), local government.
Industry/Entity Type
It Company
Look and feel

```html
<!DOCTYPE html>
<html lang="en">
<head>
<meta charset="utf-8">
<title>Brontaro Ltd – GIS Data Specialists</title>
<link rel="stylesheet" href="https://fonts.googleapis.com/css2?family=Maven+Pro:wght@500;600;700&family=Cousine&family=Tinos:ital,wght@1,700&display=swap">
<style>
  :root {
    --teal: #00666e;
    --teal-dark: #005a61;
    --teal-text: #17888f;
    --nav-active: #3aa8f0;
    --orange-top: #d96a00;
    --orange-bottom: #f7a03e;
    --white: #ffffff;
    --ink: #111111;
    --footer-ink: #0d2a2c;
    --grey-edge: #8a8a8a;
    --grey-centre: #f2f2f2;
  }
  * { margin: 0; padding: 0; box-sizing: border-box; }
  html, body { width: 1200px; height: 852px; overflow: hidden; }
  body {
    position: relative;
    background: radial-gradient(ellipse 420px 560px at 600px 60px, var(--grey-centre) 0%, #bdbdbd 55%, var(--grey-edge) 100%);
    font-family: "Maven Pro", sans-serif;
    color: var(--ink);
  }
  .contact-tab {
    position: absolute; left: 868px; top: 0; width: 99px; height: 28px;
    background: var(--teal); color: var(--white);
    border-radius: 0 0 7px 7px;
    font-size: 13px; font-weight: 600; text-align: center; line-height: 24px;
    white-space: nowrap;
  }
  .brand {
    position: absolute; left: 262px; top: 16px;
    display: flex; align-items: center; gap: 16px;
  }
  .brand-mark { width: 46px; height: 46px; border-radius: 50%; background: var(--teal); }
  .brand-name { font-size: 40px; font-weight: 700; color: var(--teal); letter-spacing: 1px; }

  .main-nav {
    position: absolute; left: 238px; top: 99px; width: 729px; height: 34px;
    background: var(--teal); border-radius: 8px 8px 0 0;
  }
  .nav-link {
    position: absolute; top: 0; height: 34px; line-height: 33px;
    color: var(--white); text-decoration: none; white-space: nowrap;
    font-size: 12.5px; font-weight: 600;
  }
  .nav-link.is-active { color: var(--nav-active); }
  .nav-link.is-active::after {
    content: ""; position: absolute; left: 50%; bottom: 0; margin-left: -6px;
    border: 6px solid transparent; border-bottom-color: var(--orange-top);
  }
  .nav-divider {
    position: absolute; top: 6px; width: 1px; height: 22px;
    background: rgba(255,255,255,0.25);
  }

  .hero {
    position: absolute; left: 238px; top: 133px; width: 729px; height: 198px;
    background: linear-gradient(var(--orange-top), var(--orange-bottom));
  }
  .hero-globe {
    position: absolute; left: 45px; top: 19px; width: 160px; height: 160px; border-radius: 50%;
    background: radial-gradient(circle at 45% 45%, #fff6a0 0%, #ffd23a 40%, #f0a020 75%, rgba(240,150,30,0.4) 100%);
  }
  .hero-title {
    position: absolute; left: 228px; top: 38px; width: 480px;
    font-size: 18px; font-weight: 700; color: var(--white); line-height: 23px;
  }
  .hero-title .accent { color: var(--teal); }
  .hero-lead {
    position: absolute; left: 228px; top: 104px; width: 480px;
    font-size: 13px; font-weight: 600; color: var(--white); line-height: 17.5px;
  }

  .content {
    position: absolute; left: 238px; top: 331px; width: 729px; height: 407px;
    background: var(--white);
  }
  .content-title {
    position: absolute; left: 38px; top: 20px;
    font-size: 19px; font-weight: 700;
  }
  .content-title .accent { color: var(--teal-text); }
  .content-body {
    position: absolute; left: 38px; top: 74px;
    font-family: "Cousine", monospace; font-size: 11.1px; line-height: 13.3px;
    white-space: pre; color: var(--ink);
  }
  .content-body .accent { color: var(--teal-text); }

  .site-footer {
    position: absolute; left: 0; top: 738px; width: 1200px; height: 114px;
    background: var(--teal-dark);
  }
  .footer-details {
    position: absolute; left: 257px; top: 11px;
    display: grid; grid-template-columns: 74px auto;
    font-size: 11.1px; line-height: 13.3px; color: var(--footer-ink);
  }
  .footer-label { font-family: "Tinos", serif; font-style: italic; font-weight: 700; font-size: 12px; }
  .footer-value { font-family: "Cousine", monospace; white-space: pre; }
  .footer-legal {
    position: absolute; left: 257px; top: 91px;
    font-family: "Cousine", monospace; font-size: 11.1px; color: var(--footer-ink);
  }
</style>
</head>
<body>
  <a class="contact-tab">Contact Us</a>

  <div class="brand">
    <span class="brand-mark"></span>
    <span class="brand-name">Brontaro</span>
  </div>

  <nav class="main-nav">
    <a class="nav-link is-active" style="left:16px">Home</a>
    <span class="nav-divider" style="left:62px"></span>
    <a class="nav-link" style="left:77px">About Us</a>
    <span class="nav-divider" style="left:147px"></span>
    <a class="nav-link" style="left:160px">Data Migration</a>
    <span class="nav-divider" style="left:265px"></span>
    <a class="nav-link" style="left:279px">Data Cleansing</a>
    <span class="nav-divider" style="left:380px"></span>
    <a class="nav-link" style="left:393px">Data Analysis</a>
    <span class="nav-divider" style="left:487px"></span>
    <a class="nav-link" style="left:500px">Data Maintenance</a>
    <span class="nav-divider" style="left:619px"></span>
    <a class="nav-link" style="left:632px">Data Quality</a>
  </nav>

  <section class="hero">
    <div class="hero-globe" role="img" aria-label="Glowing wireframe globe with golden light trails"></div>
    <h1 class="hero-title"><span class="accent">Brontaro</span> develops and supports rigorous, technologically advanced geospatial software.</h1>
    <p class="hero-lead">We have worked with over 200 companies in a myriad of market sectors - from utilities, local and central government, oil and gas, to many spheres of the marine industry.</p>
  </section>

  <main class="content">
    <h2 class="content-title">Welcome to <span class="accent">Brontaro</span></h2>
<div class="content-body"><span class="accent">Brontaro</span> was founded in 1994 by a group of geospatial software engineers
that recognised the significant value that data, and the systems used to store
and analyse this data, could bring to business.

Our Customers: We have worked with over 200 companies in a myriad of market
sectors - from utilities, local and central government, oil and gas, to many
spheres of the marine industry.

Our Pedigree: We provide a vast bank of knowledge and experience to offer
an all encompassing service. This ensures that you, as a customer, reap the
maximum benefits from your data and systems through utilising a combination
of our skilled consultants, analysts and developers that will work with you
and your requirements to help achieve your business objectives.

Our People: We have a wide ranging skill set including PRISMA 2 qualified
Project Managers, fully qualified Software Developers and Experienced Data
Consultants.

We can be on hand to help with any or all parts of your data projects via:
    -Data Consultancy
    -System Consultancy
    -Software Development</div>
  </main>

  <footer class="site-footer">
    <div class="footer-details">
      <span class="footer-label">Address:</span>
      <span class="footer-value">Brontaro Ltd Kelvinbrae Business Centre North Quay Road Kelvinbrae Westshire
      KB12 4QX,Scotland, UK</span>
      <span class="footer-label">Telephone:</span>
      <span class="footer-value">+44 (0)1500 555 210</span>
      <span class="footer-label">Fax:</span>
      <span class="footer-value">+44 (0)1500 555 219</span>
      <span class="footer-label">email:</span>
      <span class="footer-value">contact@brontaro-example.co.uk</span>
    </div>
    <p class="footer-legal">© 2010 Brontaro Ltd. Registered in Scotland No. 204417</p>
  </footer>
</body>
</html>
```